Harwell Lawyers Banner

I would like to have a graphic design created for a company banner. The company is Harwell Lawyers and the website is https://harwelllawyers-example.com.au/ We would like a professional banner we are able to put up at events to advertise the company.
The banner size is 800mm wide by 2000mm high so please keep the design inside these constraints.

```html
<!DOCTYPE html>
<html lang="en">
<head>
<meta charset="utf-8">
<title>Harwell Lawyers – Event Banner</title>
<link href="https://fonts.googleapis.com/css2?family=Barlow+Semi+Condensed:wght@300;400;500;600&family=Open+Sans:wght@700&display=swap" rel="stylesheet">
<style>
  :root {
    --stage: #e9e6e4;
    --banner-dark: #1c2124;
    --banner-deep: #121517;
    --brand-blue: #2ea8d8;
    --accent-orange: #f6a623;
    --text-white: #ffffff;
    --photo-light: #b9b9b9;
    --photo-mid: #6d6d6d;
  }
  * { box-sizing: border-box; margin: 0; padding: 0; }
  html, body {
    width: 1200px; height: 1009px; overflow: hidden;
    background: var(--stage);
  }
  .banner {
    position: absolute; left: 412px; top: 34px;
    width: 376px; height: 940px;
    background: var(--banner-dark);
    overflow: hidden;
    font-family: "Barlow Semi Condensed", sans-serif;
    color: var(--text-white);
  }
  .brand {
    position: absolute; right: 40px; top: 48px;
    text-align: right; font-weight: 300; color: var(--text-white);
  }
  .brand-name { display: block; font-size: 66px; line-height: 1; letter-spacing: 1px; }
  .brand-sub { display: block; font-size: 24px; letter-spacing: 6px; margin-top: 4px; }

  .statement {
    position: absolute; left: 46px; top: 184px; width: 320px;
    font-weight: 600; font-size: 20.5px; line-height: 27.5px;
    text-transform: uppercase; letter-spacing: 0.1px;
  }
  .statement .blue { color: var(--brand-blue); }
  .corner { position: absolute; }
  .corner-open { left: 21px; top: 166px; }
  .corner-close { left: 314px; top: 246px; }

  .services {
    position: absolute; left: 0; top: 314px; width: 376px;
    display: grid; grid-template-columns: 188px 188px; row-gap: 18px;
  }
  .service { display: flex; flex-direction: column; align-items: center; }
  .service:nth-child(odd) { padding-right: 14px; }
  .service:nth-child(even) { padding-left: 14px; }
  .service-icon { width: 66px; height: 66px; }
  .service-label {
    margin-top: 24px; font-size: 15.5px; font-weight: 500;
    line-height: 20px; text-align: center;
  }

  .team-photo {
    position: absolute; left: 0; top: 600px; width: 376px; height: 318px;
    background:
      linear-gradient(to bottom, var(--banner-dark) 0%, rgba(28,33,36,0) 22%, rgba(28,33,36,0) 62%, var(--banner-deep) 100%),
      linear-gradient(to bottom, var(--photo-light) 20%, var(--photo-mid) 55%, #2a2a2a 100%);
  }
  .website {
    position: absolute; left: 0; width: 376px; top: 860px;
    text-align: center; font-family: "Open Sans", sans-serif;
    font-weight: 700; font-size: 19px; color: var(--text-white);
  }
  .website .blue { color: var(--brand-blue); }
  .base-band {
    position: absolute; left: 0; bottom: 0; width: 376px; height: 21px;
    background: var(--brand-blue);
  }
</style>
</head>
<body>
<main class="banner">
  <div class="brand">
    <span class="brand-name">HARWELL</span>
    <span class="brand-sub">LAWYERS</span>
  </div>

  <svg class="corner corner-open" width="32" height="32" viewBox="0 0 32 32">
    <path d="M2 30 V2 H30" fill="none" stroke="var(--brand-blue)" stroke-width="2.5"/>
    <path d="M7 30 V7 H30" fill="none" stroke="var(--brand-blue)" stroke-width="1.2"/>
  </svg>
  <p class="statement">
    <span class="blue">Harwell Lawyers is a</span> Leading<br>
    Commercial law firm <span class="blue">located</span><br>
    <span class="blue">in Calder City, Eastmoor</span>
  </p>
  <svg class="corner corner-close" width="30" height="30" viewBox="0 0 30 30">
    <path d="M0 27 H27 V0" fill="none" stroke="var(--brand-blue)" stroke-width="5"/>
  </svg>

  <section class="services">
    <div class="service">
      <svg class="service-icon" viewBox="0 0 66 66" fill="none" stroke="var(--accent-orange)">
        <path d="M3 22 V3 H22" stroke-width="4"/><path d="M44 3 H63 V22" stroke-width="1.4"/>
        <path d="M63 44 V63 H44" stroke-width="4"/><path d="M22 63 H3 V44" stroke-width="1.4"/>
        <rect x="22" y="16" width="22" height="30" stroke-width="1.4"/>
        <path d="M27 23 H39 M27 29 H39 M27 35 H39 M27 41 H35" stroke-width="1.4"/>
      </svg>
      <p class="service-label">Private Clients and<br>Family Businesses</p>
    </div>
    <div class="service">
      <svg class="service-icon" viewBox="0 0 66 66" fill="none" stroke="var(--accent-orange)">
        <path d="M3 22 V3 H22" stroke-width="4"/><path d="M44 3 H63 V22" stroke-width="1.4"/>
        <path d="M63 44 V63 H44" stroke-width="4"/><path d="M22 63 H3 V44" stroke-width="1.4"/>
        <path d="M18 32 L33 18 L48 32 M22 29 V44 H44 V29" stroke-width="1.4"/>
        <rect x="29" y="34" width="8" height="10" stroke-width="1.4"/>
      </svg>
      <p class="service-label">Startups and<br>New Businesses</p>
    </div>
    <div class="service">
      <svg class="service-icon" viewBox="0 0 66 66" fill="none" stroke="var(--accent-orange)">
        <path d="M3 22 V3 H22" stroke-width="4"/><path d="M44 3 H63 V22" stroke-width="1.4"/>
        <path d="M63 44 V63 H44" stroke-width="4"/><path d="M22 63 H3 V44" stroke-width="1.4"/>
        <circle cx="33" cy="24" r="4" stroke-width="1.4"/><circle cx="24" cy="28" r="3" stroke-width="1.4"/><circle cx="42" cy="28" r="3" stroke-width="1.4"/>
        <path d="M16 34 Q18 46 28 50 M50 34 Q48 46 38 50" stroke-width="1.4"/>
      </svg>
      <p class="service-label">Established<br>Organisations</p>
    </div>
    <div class="service">
      <svg class="service-icon" viewBox="0 0 66 66" fill="none" stroke="var(--accent-orange)">
        <path d="M3 22 V3 H22" stroke-width="4"/><path d="M44 3 H63 V22" stroke-width="1.4"/>
        <path d="M63 44 V63 H44" stroke-width="4"/><path d="M22 63 H3 V44" stroke-width="1.4"/>
        <rect x="15" y="16" width="20" height="13" rx="2" stroke-width="1.4"/>
        <rect x="31" y="22" width="20" height="13" rx="2" stroke-width="1.4"/>
        <path d="M14 48 H52 M24 48 V42 H32 V48 M36 48 V42 H44 V48" stroke-width="1.4"/>
      </svg>
      <p class="service-label">Professional<br>Advisors</p>
    </div>
  </section>

  <div class="team-photo" role="img" aria-label="Black and white photo of professionals silhouetted against a city skyline through tall office windows"></div>

  <p class="website">www.<span class="blue">harwelllawyers-example</span>.com.au</p>
  <div class="base-band"></div>
</main>
</body>
</html>
```